High-Class Professional Letterhead for a solo doctor's practice.

Please create a letterhead design that includes my logo, and options of my light blue/black color scheme and black and gold so I can choose between the two. I would like my Contact information on the top or bottom of the letterhead somewhere:
Delia Forsk, M.D.
Hand and Upper Extremity Surgeon
4382 NW 58th Lane, Suite 307
Tamarac, FL 33498
Phone: (954) 316-8842
Fax: (800) 629-4087
www.dforskgrip.example

Also on the bottom of the letterhead, there should be 2 different versions:
one that is blank, and one that has a signature spot on the bottom so I can sign:
Delia Forsk, M.D.
Board Certified Orthopaedic Hand Surgeon

I am going for classy/professional. I want other doctors and or lawyers to look at my letterhead and want to work with me. Again, professional, classy, clean. I do like black and gold but I could see what the blue like my other business card looks like too. Please do what most people do for letterheads--I'm not sure if the signature line should be on there? Or should be blank? I have no clue

Target Market(s)

Doctors and Lawyers

Industry/Entity Type

Medicine

Colors
0054AA
0677BA
7BADD7
CADEEF
E8F1F8

Requirements
Must have
• High class, professional, appealing

```html
<!DOCTYPE html>
<html lang="en">
<head>
<meta charset="utf-8">
<title>Delia Forsk, M.D. — Letterhead</title>
<link rel="stylesheet" href="https://fonts.googleapis.com/css2?family=Poppins:wght@500;600&family=Questrial&family=Open+Sans:wght@600&family=Lato:wght@400&display=swap">
<style>
  :root {
    --brand-blue: #1f9bd7;
    --ink: #111418;
    --icon-bg: #1c2430;
    --text-grey: #8e8e8e;
    --name-grey: #9c9c9c;
    --body-grey: #8a8a8a;
    --paper: #ffffff;
    --backdrop: #ecedef;
  }
  * { margin: 0; padding: 0; box-sizing: border-box; }
  html, body { width: 1068px; height: 1200px; overflow: hidden; background: var(--backdrop); }
  .canvas { position: relative; width: 1068px; height: 1200px; }
  .letterhead {
    position: absolute; left: 106px; top: 0;
    width: 855px; height: 1200px;
    background: var(--paper);
    overflow: hidden;
  }
  .brand-tab { position: absolute; left: 80px; top: 0; width: 171px; height: 230px; }
  .brand-name {
    position: absolute; left: 80px; top: 86px; width: 171px; height: 140px;
    display: flex; align-items: center; justify-content: center;
    font-family: "Poppins", sans-serif; font-weight: 600; font-size: 19px;
    color: var(--ink); letter-spacing: 0.5px; text-align: center; line-height: 1.15;
  }
  .contact-list {
    position: absolute; left: 629px; top: 112px;
    list-style: none;
    font-family: "Lato", sans-serif; font-size: 16px; color: var(--text-grey);
  }
  .contact-list li { display: flex; align-items: center; height: 20px; margin-bottom: 11px; }
  .contact-icon {
    width: 20px; height: 20px; margin-right: 6px;
    background: var(--icon-bg); border-radius: 2px;
    display: flex; align-items: center; justify-content: center;
  }
  .sender {
    position: absolute; left: 78px; top: 323px;
    font-family: "Questrial", sans-serif; color: var(--text-grey); font-size: 14px;
  }
  .sender-name {
    font-family: "Poppins", sans-serif; font-weight: 600; font-size: 24px;
    color: var(--name-grey); line-height: 1; margin-bottom: 10px;
  }
  .sender p { line-height: 25px; }
  .sender .address { line-height: 19px; margin-top: 3px; }
  .letter-date {
    position: absolute; right: 66px; top: 430px;
    font-family: "Open Sans", sans-serif; font-weight: 600; font-size: 16.5px; color: var(--text-grey);
  }
  .letter-body {
    position: absolute; left: 73px; top: 482px; width: 716px;
    font-family: "Questrial", sans-serif; font-size: 14.6px; line-height: 18px;
    color: var(--body-grey); text-align: justify;
  }
  .letter-body p + p { margin-top: 18px; }
  .letter-body p.tight { margin-top: 0; }
  .letter-body p.spaced { margin-top: 36px; }
  .sign-off { position: absolute; left: 88px; top: 860px; width: 240px; text-align: center; }
  .sign-name { font-family: "Poppins", sans-serif; font-weight: 600; font-size: 19px; color: var(--ink); line-height: 1.1; }
  .sign-name .first { color: var(--brand-blue); }
  .sign-title { font-family: "Questrial", sans-serif; font-size: 11px; color: var(--ink); margin-top: 4px; }
  .signature-area {
    position: absolute; left: 135px; top: 916px; width: 146px; height: 92px;
    background: linear-gradient(135deg, #f4f4f4, #e6e6e6);
  }
  .footer-rule { position: absolute; left: 0; top: 1165px; width: 468px; height: 4px; background: var(--ink); }
  .footer-band {
    position: absolute; left: 466px; top: 1142px; width: 389px; height: 30px;
    background: var(--brand-blue);
    clip-path: polygon(25px 0, 100% 0, 100% 100%, 0 100%);
    font-family: "Lato", sans-serif; font-size: 13px; color: #fff;
    display: flex; align-items: center; padding-left: 33px;
  }
</style>
</head>
<body>
<div class="canvas">
  <main class="letterhead">
    <header>
      <svg class="brand-tab" viewBox="0 0 171 230" aria-hidden="true">
        <path d="M0 0 H171 V117 A94 94 0 0 0 0 117 Z" fill="var(--brand-blue)"/>
        <circle cx="85.5" cy="157" r="66" fill="none" stroke="var(--ink)" stroke-width="3"/>
      </svg>
      <div class="brand-name">Forsk<br>Hand</div>

      <ul class="contact-list">
        <li>
          <span class="contact-icon">
            <svg width="12" height="12" viewBox="0 0 24 24"><path fill="#fff" d="M6.6 10.8a15.1 15.1 0 0 0 6.6 6.6l2.2-2.2a1 1 0 0 1 1-.25 11.4 11.4 0 0 0 3.6.57 1 1 0 0 1 1 1V20a1 1 0 0 1-1 1A17 17 0 0 1 3 4a1 1 0 0 1 1-1h3.5a1 1 0 0 1 1 1 11.4 11.4 0 0 0 .57 3.6 1 1 0 0 1-.25 1z"/></svg>
          </span>(954) 316-8842
        </li>
        <li>
          <span class="contact-icon">
            <svg width="13" height="13" viewBox="0 0 24 24"><path fill="#fff" d="M7 3h10v4H7zM4 8h16a2 2 0 0 1 2 2v6h-4v5H6v-5H2v-6a2 2 0 0 1 2-2zm4 8v3h8v-3z"/></svg>
          </span>(800) 629-4087
        </li>
        <li>
          <span class="contact-icon">
            <svg width="11" height="12" viewBox="0 0 24 24"><path fill="#fff" d="M5 2l14 11-6 .8 3.5 7-2.6 1.2-3.4-7L5 20z"/></svg>
          </span>www.dforskgrip.example
        </li>
      </ul>
    </header>

    <section class="sender">
      <h1 class="sender-name">Delia Forsk, M.D.</h1>
      <p>0198-372-554</p>
      <p>office@forskhand.example</p>
      <p class="address">5610 Harlow Ave. Suite<br>214 Dallas, TX 75201</p>
    </section>
    <p class="letter-date">04 December, 2023</p>

    <article class="letter-body">
      <p>Lorem ipsum dolor sit amet, consectetuer adipiscing elit, sed diam nonummy nibh euismod tincidunt ut laoreet dolore magna aliquam erat volutpat. Ut wisi enim ad minim veniam, quis nostrud exerci tation ullamcorper suscipit lobortis nisl ut aliquip ex ea commodo consequat. Duis autem vel eum iriure dolor in hendrerit in vulputate velit esse molestie consequat, vel illum dolore eu feugiat nulla facilisis at vero eros et accumsan et iusto odio dignissim qui blandit praesent luptatum zzril delenit augue duis dolore te feugait nulla facilisi.</p>
      <p>Lorem ipsum dolor sit amet, cons ectetuer adipiscing elit, sed diam nonummy nibh euismod tincidunt ut laoreet dolore magna aliquam erat volutpat. Ut wisi enim ad minim veniam, quis nostrud exerci tation ullamcorper suscipit lobortis nisl ut aliquip ex ea commodo consequat.</p>
      <p class="tight">Lorem ipsum dolor sit amet, consectetuer adipiscing elit, sed diam nonummy nibh euismod tincidunt ut laoreet dolore magna aliquam erat</p>
      <p class="spaced">Lorem ipsum dolor sit amet, cons ectetuer adipiscing elit, sed diam nonummy nibh euismod tincidunt ut laoreet dolore magna aliquam erat volutpat. Ut wisi enim ad minim veniam, quis nostrud exerci tation ullamcorper suscipit lobortis nisl ut aliquip ex ea commodo consequat. Lorem ipsum dolor sit zamet, con-sectetuer adipiscing elit, sed diam nonummy nibh euismod tincidunt.</p>
    </article>

    <section class="sign-off">
      <p class="sign-name"><span class="first">Delia</span> Forsk, M.D.</p>
      <p class="sign-title">Board Certified Orthopaedic Hand Surgeon</p>
    </section>
    <div class="signature-area" role="img" aria-label="Handwritten signature of Delia Forsk"></div>

    <footer>
      <div class="footer-rule"></div>
      <div class="footer-band">4382 NW 58th Lane, Suite 307 Tamarac, FL 33498</div>
    </footer>
  </main>
</div>
</body>
</html>
```